MOSLEN Environmental needs an upgrade to its current business cards design

We need an upgrade to our current business cards design, where the MOSLEN acronym is included, as possible and not being overloaded.
MOSLEN Environmental is an Environmental Consultancy Firm based in Sydney.
We would like to see creative designs different from the standard type of business cards (for example, rounded edges, different to standard size of common business cards.

Target Market(s)

industrial companies (oil & gas, petrochemical, mining, insolvency, finance and manufacturing), developers, architect firms, law firms.

Industry/Entity Type

Business

Contact Information for Business Card

logos (brand and acronym), if they don't appear overloaded.
name
role
name of company (MOSLEN Environmental),
address (Level 3, Suite 3C, 47-49 Dorrigan Lane, Wexmoor, NSW, 2188) landline (02 7314 2986)
mobile (staff member)
email (staff member) and
website (www.moslengreen.example).
Include: Contaminated Land, Site Remediation, Groundwater Assessment, Health and Ecological Risk Assessments, Acid Sulfate Soils, Waste Classification.

Font styles to use
Serif
Sans Serif

Requirements
Must have
• A creative design different to the standard type of business cards.
Nice to have
• Rounded edges
• Different size of business cards rather than the standard size.
Should not have
• Preferable not to use white colour background, unless it is required from a creative design proposed.
• Not an overloaded design.
• Avoid black colours

```html
<!DOCTYPE html>
<html lang="en">
<head>
<meta charset="utf-8">
<title>MOSLEN Environmental – Business Card</title>
<link rel="stylesheet" href="https://fonts.googleapis.com/css2?family=Open+Sans:wght@400;600;700&family=Arimo:wght@700&display=swap">
<style>
  :root {
    --stage-top: #2b2b2b;
    --stage-bottom: #050505;
    --card-white: #ffffff;
    --brand-green: #6fa41c;
    --bright-green: #8cc800;
    --slate: #5e5f5f;
    --ink: #333333;
    --acronym-ink: #444444;
  }
  * { margin: 0; padding: 0; box-sizing: border-box; }
  html, body { width: 1200px; height: 900px; overflow: hidden; }
  body {
    background: linear-gradient(to bottom, var(--stage-top), #1a1a1a 55%, var(--stage-bottom));
    position: relative;
    font-family: "Open Sans", Arial, sans-serif;
  }
  .card {
    position: absolute;
    top: 306px;
    height: 271px;
    border-radius: 12px;
  }
  .card-front { left: 149px; width: 439px; background: var(--card-white); }
  .card-back {
    left: 608px; width: 441px;
    background: linear-gradient(to bottom, var(--bright-green) 0%, #7fb30a 30%, #6e7e48 65%, var(--slate) 100%);
  }

  /* acronym column */
  .acronym { position: absolute; left: 52px; top: 50px; }
  .acronym-row { display: flex; align-items: center; height: 29px; }
  .acronym-letter {
    width: 32px;
    font-family: "Arimo", Arial, sans-serif;
    font-weight: 700;
    font-size: 27px;
    color: var(--slate);
    text-align: center;
  }
  .acronym-word {
    margin-left: 2px;
    font-family: "Arimo", Arial, sans-serif;
    font-weight: 700;
    font-size: 12.5px;
    color: var(--acronym-ink);
  }

  /* contact column */
  .contact { position: absolute; left: 226px; top: 46px; color: var(--ink); }
  .person-name { font-size: 15px; font-weight: 600; color: var(--brand-green); line-height: 18px; }
  .person-role { font-size: 12px; line-height: 15px; }
  .company-name { margin-top: 20px; font-size: 12px; font-weight: 700; color: var(--brand-green); line-height: 16px; }
  .address { font-size: 12px; line-height: 16px; }
  .contact-list { list-style: none; margin-top: 6px; }
  .contact-list li { display: flex; align-items: center; font-size: 12px; line-height: 16px; }
  .contact-list svg { width: 10px; height: 10px; margin-right: 6px; fill: var(--brand-green); }

  /* back */
  .brand-name {
    position: absolute; top: 60px; left: 0; right: 0;
    text-align: center;
    font-family: "Open Sans", Arial, sans-serif;
    font-weight: 700;
    color: var(--slate);
    line-height: 1;
  }
  .brand-name .brand-main { display: block; font-size: 44px; letter-spacing: 1px; }
  .brand-name .brand-sub { display: block; font-size: 13px; letter-spacing: 3.5px; margin-top: 4px; }
  .services {
    position: absolute; top: 164px; left: 0; right: 0;
    text-align: center;
    color: #ffffff;
    font-size: 12px;
    line-height: 16px;
  }
</style>
</head>
<body>

<section class="card card-front">
  <div class="acronym">
    <div class="acronym-row"><span class="acronym-letter">M</span><span class="acronym-word">ONITORING</span></div>
    <div class="acronym-row"><span class="acronym-letter">O</span><span class="acronym-word">F</span></div>
    <div class="acronym-row"><span class="acronym-letter">S</span><span class="acronym-word">OIL,</span></div>
    <div class="acronym-row"><span class="acronym-letter">L</span><span class="acronym-word">AND (AND)</span></div>
    <div class="acronym-row"><span class="acronym-letter">E</span><span class="acronym-word">NVIRONMENTAL</span></div>
    <div class="acronym-row"><span class="acronym-letter">N</span><span class="acronym-word">ETWORKS</span></div>
  </div>

  <div class="contact">
    <p class="person-name">Daniel Hargrove</p>
    <p class="person-role">Managing Director</p>
    <p class="company-name">MOSLEN Environmental</p>
    <p class="address">Level 3, Suite 3C, 47-49 Dorrigan Lane,<br>Wexmoor, NSW, 2188</p>
    <ul class="contact-list">
      <li><svg viewBox="0 0 10 10"><rect x="2.5" y="0" width="5" height="10" rx="1"/></svg>0198 765 432</li>
      <li><svg viewBox="0 0 10 10"><path d="M2 0 L4 2.5 L3 4 Q4.5 6 6 7 L7.5 6 L10 8 L8.5 10 Q2 9 0 1.5 Z"/></svg>044-987 654 321</li>
      <li><svg viewBox="0 0 10 10"><path d="M0 2 H10 V8 H0 Z M0 2 L5 6 L10 2" /></svg>info@moslengreen.example</li>
      <li><svg viewBox="0 0 10 10"><circle cx="5" cy="5" r="5"/></svg>www.moslengreen.example</li>
    </ul>
  </div>
</section>

<section class="card card-back">
  <h1 class="brand-name"><span class="brand-main">MOSLEN</span><span class="brand-sub">ENVIRONMENTAL</span></h1>
  <p class="services">
    Contaminated Land | Site Remediation | Groundwater Assessment<br>
    Health and Ecological Risk Assessments | Acid Sulfate Soils<br>
    Waste Classification.
  </p>
</section>

</body>
</html>
```